Design Creative Banner or Gif Ads. 3 Designs To Be Selected

Come up with some creative banner ads for stonewell.co.nz

*At least 3 different winning banners will be chosen*

Please provide banner ads / gif ads in common google ads / website banner formats.

They can be gif or static but must stand out while still maintaining clear clean text and visuals, with a premium professional feel (please avoid clip art or anything that gives a cheap message).

Please keep in mind that these will likely be small ads so text needs to be large and if there's there a lot of text then use multiple frames/ pages as submit as a gif.

Style
Minimal & clean lines
Architectural or realistic images
Avoid cartoon styles, clipart, or anything that looks cheap

Font
Nexa or Montserrat or similar

Tone
Premium, serious, trustworthy — fits new builds

Colours
Option 1: Deep Navy (trust & quality) & lighter blues and warm grey
Option 2: Open to bright colours to help the ads stand out, such as (but not limited to) bright pink with black, yellow, fluorescent green, provided the messaging is still done professionally.
Our logo is attached (Stone Well Logo)

Display Sizes
Ad specs for file sizes should be file formats like JPEG, GIF, and PNG, with animations limited to a max of 30 seconds or less.
We will need several different ad sizes provided for each of the 3 selected winning designs.

• Medium Rectangle: 300 × 250 pixels
• Leaderboard: 728 × 90 pixels
• Desktop Banner ad image: (640x360 pixels)
• Desktop Banner ad image 2: (300x600 pixels)
• Possibly one or two other sizes

Flexibility to be creative
The ad text, words, upper/lower case, layout, colour, theme, and images can be adjusted to how you think it will look best. The follow example ads are just examples of what we are after but we are keen to see what you can create.

Recommendations at this point:
1. Avoid text heavy
2. Looking for more Gif ads
3. Imaging: if possible use real stock photo's rather than AI

Themes:

1
Building Soon? Start Here
Free Build Planning Pack:
✓ Build Cost Calculator
✓ Hidden Cost Checklist
✓ Builder Comparison Guide
Build With Confidence
Download Free

2
Before You Choose A Builder
Compare Price, Scope, Risk & Value
Avoid Costly Mistakes
Choose The Right Builder With Confidence
Download The Free Guide

3
Planning A New Build?
Avoid These Common Mistakes:
✗ Hidden Exclusions
✗ Missing Scope
✗ Unrealistic Allowances
✗ Budget Blowouts
Download The Free Guide

4
Before You Buy Land
Know what it could cost to build.
Avoid Costly Building Mistakes
Download Our Free Guides

5
Know Your Build Budget?
• Free Build Cost Calculator
• Hidden Cost Checklist
• Build Planning Tools
Calculate Costs (Download)

Target Market(s)

Landowners looking to build

Industry/Entity Type

Building

Font styles to use
Other font styles liked:
• Nexa or Montserrat or similar

Requirements
Should not have
• Avoid cartoon styles, clipart, or anything that looks cheap

```html
<!DOCTYPE html>
<html lang="en">
<head>
<meta charset="UTF-8">
<title>Building Soon? – Free Build Planning Pack</title>
<link href="https://fonts.googleapis.com/css2?family=Montserrat:wght@600;700;800&display=swap" rel="stylesheet">
<style>
  :root {
    --royal-blue: #1240b8;
    --panel-blue: #0c3bb3;
    --navy: #0b2a8c;
    --white: #ffffff;
    --badge-yellow: #f8ec3c;
    --badge-edge: #e2c82a;
    --sky-top: #eef4f8;
    --sky-low: #dfe8ee;
    --city-grey: #b9c3c9;
    --tree-green: #6f8f3a;
    --grass-light: #a8c85a;
    --grass-deep: #7faa3a;
  }
  * { margin: 0; padding: 0; box-sizing: border-box; }
  html, body {
    width: 1200px;
    height: 675px;
    overflow: hidden;
    background: var(--white);
  }
  .banner {
    position: relative;
    width: 1200px;
    height: 675px;
    overflow: hidden;
    font-family: "Montserrat", Arial, sans-serif;
  }
  .banner__scene {
    position: absolute;
    inset: 0;
    background: linear-gradient(
      to bottom,
      var(--sky-top) 0%,
      var(--sky-low) 38%,
      var(--city-grey) 62%,
      var(--tree-green) 76%,
      var(--grass-light) 82%,
      var(--grass-deep) 100%
    );
  }
  .headline {
    position: absolute;
    left: 92px;
    top: 76px;
    color: var(--royal-blue);
    font-weight: 800;
    font-size: 86px;
    line-height: 1.17;
    letter-spacing: 0.5px;
  }
  .pack-panel {
    position: absolute;
    left: 68px;
    top: 368px;
    width: 450px;
    height: 198px;
    background: var(--panel-blue);
    color: var(--white);
    padding: 18px 22px;
    font-weight: 600;
    font-size: 25px;
    line-height: 37.5px;
  }
  .pack-panel__list { list-style: none; }
  .pack-panel__list li::before { content: "\2713\00a0"; }
  .cta-badge {
    position: absolute;
    left: 887px;
    top: 356px;
    width: 281px;
    height: 272px;
  }
  .cta-badge svg { position: absolute; inset: 0; }
  .cta-badge__text {
    position: absolute;
    inset: 0;
    display: flex;
    flex-direction: column;
    justify-content: center;
    align-items: center;
    text-align: center;
    color: var(--navy);
    font-weight: 700;
    font-size: 24px;
    line-height: 31px;
    padding-top: 6px;
  }
</style>
</head>
<body>
  <div class="banner">
    <div class="banner__scene" role="img" aria-label="Photo of a sunny city park: green lawn and trees in front of a modern high-rise skyline under a bright sky"></div>

    <h1 class="headline">Building<br>Soon?</h1>

    <div class="pack-panel">
      <p class="pack-panel__title">Free Build Planning Pack:</p>
      <ul class="pack-panel__list">
        <li>Build Cost Calculator</li>
        <li>Hidden Cost Checklist</li>
        <li>Builder Comparison Guide</li>
      </ul>
    </div>

    <div class="cta-badge">
      <svg viewBox="0 0 281 272" width="281" height="272" aria-hidden="true">
        <polygon points="140,2 200,26 264,42 279,110 256,176 240,234 180,254 140,270 96,250 40,234 16,176 2,110 20,44 80,26"
                 fill="var(--badge-yellow)" stroke="var(--badge-edge)" stroke-width="3" stroke-linejoin="round"/>
      </svg>
      <div class="cta-badge__text">
        <span>Build With</span>
        <span>Confidence</span>
        <span>Download Free</span>
      </div>
    </div>
  </div>
</body>
</html>
```